Commercial Energy Advice for the Property Market

We need an a5 ad for magazine

Target Market(s)

Real estate

Industry/Entity Type

Real Estate Agent

Colors

Designer to choose colors to be used in the design.

Requirements
Must have
• Our logo www.ledgerwise.co.uk
• Must have text below
• Must have a list of our services as listed in our website
• Attachment is a similar company add
Nice to have
• Ledger Wise can help you manage MEES and EPC Risk
• With MEES fast approaching and the importance and value of data, Ledger Wise have created software LWTrack to help manage your EPC Risk in order to effectively mitigate risk with minimum capital cost. LW are able to support you through each stage of the property life cycle whether it be:-
• Acquisition
• Selling
• New lettings
• Refurbishment
• Property Management
• Lease advisory
Should not have
• Cheesy designs

```html
<!DOCTYPE html>
<html lang="en">
<head>
<meta charset="utf-8">
<title>Ledger Wise – EPC Risk Ad</title>
<link rel="stylesheet" href="https://fonts.googleapis.com/css2?family=Roboto+Slab:wght@300;400;700&display=swap">
<style>
  :root {
    --ink: #1e1e1e;
    --white: #ffffff;
    --green: #4caf50;
    --yellow: #fdcb58;
    --pink: #d47eb1;
    --lavender: #b9a3d3;
    --rule: #5cb85c;
  }
  * { margin: 0; padding: 0; box-sizing: border-box; }
  html, body { width: 846px; height: 1200px; overflow: hidden; background: var(--white); }
  .ad {
    position: relative; width: 846px; height: 1200px; overflow: hidden;
    font-family: "Roboto Slab", Georgia, serif; color: var(--ink);
  }
  .hero {
    position: absolute; left: 0; top: 0; width: 846px; height: 606px;
    background:
      linear-gradient(180deg, rgba(0,0,0,0) 0%, rgba(0,0,0,0) 55%, rgba(20,10,10,0.85) 82%, #100a0a 100%),
      radial-gradient(ellipse at 95% 90%, #ffd27a 0%, #f3a04a 18%, rgba(236,140,80,0) 50%),
      linear-gradient(180deg, #3f6fc2 0%, #6f7fd0 18%, #9a86c8 35%, #d99aa6 55%, #f2b27a 72%, #b45a2c 100%);
  }
  .hero-url {
    position: absolute; right: 57px; top: 55px;
    font-size: 14px; line-height: 18px; font-weight: 300; color: var(--white);
  }
  .headline {
    position: absolute; left: 57px; top: 140px;
    font-size: 44px; line-height: 52px; font-weight: 700; color: var(--white);
  }
  .colour-band { position: absolute; left: 0; top: 606px; width: 846px; height: 23px; display: flex; }
  .colour-band span { display: block; height: 100%; }
  .band-green { width: 459px; background: var(--green); }
  .band-yellow { width: 129px; background: var(--yellow); }
  .band-pink { width: 128px; background: var(--pink); }
  .band-lavender { width: 130px; background: var(--lavender); }
  .intro {
    position: absolute; left: 57px; top: 673px; width: 732px;
    font-size: 16px; line-height: 22px; font-weight: 300; text-align: justify;
  }
  .list { position: absolute; left: 57px; list-style: none; font-size: 16px; line-height: 20.5px; font-weight: 300; }
  .list li { position: relative; padding-left: 37px; }
  .list li::before { content: "•"; position: absolute; left: 2px; }
  .lifecycle { top: 780px; }
  .services-title { position: absolute; left: 57px; top: 925px; font-size: 16px; line-height: 20.5px; font-weight: 300; }
  .services { top: 945px; }
  .brand-name {
    position: absolute; right: 57px; top: 1022px;
    font-size: 36px; line-height: 44px; font-weight: 700; color: var(--ink);
    white-space: nowrap;
  }
  .rule { position: absolute; left: 57px; top: 1104px; width: 732px; height: 1px; background: var(--rule); }
  .contact-email { position: absolute; left: 57px; top: 1124px; font-size: 16px; line-height: 20px; font-weight: 300; }
  .contact-address { position: absolute; left: 57px; top: 1147px; font-size: 12px; line-height: 16px; font-weight: 700; }
</style>
</head>
<body>
<main class="ad">
  <div class="hero" role="img" aria-label="Photograph of construction workers silhouetted on scaffolding and steel beams against a sunset sky"></div>
  <p class="hero-url">www.ledgerwise.co.uk</p>
  <h1 class="headline">Your EPC Risks<br>are in our hands.</h1>

  <div class="colour-band">
    <span class="band-green"></span><span class="band-yellow"></span><span class="band-pink"></span><span class="band-lavender"></span>
  </div>

  <p class="intro">Ledger Wise can help you manage MEES and EPC Risk. With MEES fast approaching and the importance and value of data, Ledger Wise have created software LWTrack to help manage your EPC Risk in order to effectively mitigate risk with minimum capital cost. LW are able to support you through each stage of the property life cycle whether it be:</p>

  <ul class="list lifecycle">
    <li>Acquisition</li>
    <li>Selling</li>
    <li>New lettings</li>
    <li>Refurbishment</li>
    <li>Property Management</li>
    <li>Lease advisory</li>
  </ul>

  <p class="services-title">Ledger Wise services include;</p>
  <ul class="list services">
    <li>EPC</li>
    <li>EPC+</li>
    <li>EPC Risk Profiling</li>
    <li>Asbestos</li>
    <li>Air con Surveys TM44</li>
    <li>Floor Plans</li>
    <li>Esos Energy Audit</li>
  </ul>

  <p class="brand-name">Ledger Wise</p>

  <div class="rule"></div>
  <p class="contact-email">info@ledgerwise.co.uk</p>
  <p class="contact-address">Harbour House, 48-52 Kestrel Street, London, EC2A 4QN</p>
</main>
</body>
</html>
```